Indian Wedding Invitation

Hello Designers,

We are looking for a fantastic graphic designer to help us come up with our very own bespoke wedding invitation.

We have a logo which we would like to use (see attached) and a very good idea of the style of invitation we are after.

Specification:

- We would like the wedding invitation to be A5 (landscape) with a pocket within it to allow for 3 inserts.
- The pocket should be at the bottom when you open up the card
- The first insert will be A5, the second will be slightly smaller and then the final one will be slightly smaller than that (so that you can see that there are 3 invites included in the invite) - see attached images for what I am referring to
- We will need all 3 of these to match the design of the card
- Once you open the card, the top of the card will contain some content - like details of where we are getting married / timings / rsvp information etc.
- Content will be provided once we have a view of the design

See attached images for the type of designs we are looking for. Also see: http://www.lorvanpress.co.uk/pocket-fold-invitations.html

We are looking for a fresh approach to this card.

We do not have any preference on colour, but it should work well with the logo design that we have.

Hope this is enough information to get you started. Any questions, please drop me a message or email me on tkelmore@fenwickpost.com. I'm usually very quick at responding.

Thanks!

Industry/Entity Type

Graphic Designer

Requirements
Must have
• Classy and high-end look and feel

Use of subtle colours - nothing bright

```html
<!DOCTYPE html>
<html lang="en">
<head>
<meta charset="utf-8">
<title>Kavita &amp; Rohan – Wedding Invitation</title>
<link rel="stylesheet" href="https://fonts.googleapis.com/css2?family=Pinyon+Script&family=Cormorant+SC:wght@500;600&display=swap">
<style>
  :root {
    --backdrop: #ece8e1;
    --cover-brown: #4b3327;
    --cover-stripe: #5a3f31;
    --panel-gold: #e2cd9a;
    --panel-gold-light: #eddcb3;
    --pocket-gold: #cdb07a;
    --pocket-gold-light: #dcc390;
    --insert-cream: #f4eee2;
    --insert-cream-2: #efe7d7;
    --insert-cream-3: #e9dfcc;
    --ink: #2c211b;
    --gold-ink: #a77a2c;
    --ornament-tint: #e6d6b4;
    --crystal: #cfe3ea;
  }
  * { margin: 0; padding: 0; box-sizing: border-box; }
  html, body { width: 1200px; height: 848px; overflow: hidden; }
  body {
    background: var(--backdrop);
    position: relative;
    font-family: "Cormorant SC", "Times New Roman", serif;
    color: var(--ink);
  }
  .stripes {
    background: repeating-linear-gradient(90deg, var(--cover-brown) 0 3px, var(--cover-stripe) 3px 5px);
  }

  /* Front cover */
  .cover {
    position: absolute;
    left: 40px; top: 233px;
    width: 540px; height: 382px;
    box-shadow: 0 2px 8px rgba(60, 40, 25, .18);
  }
  .cover-panel {
    position: absolute;
    left: 78px; top: 68px;
    width: 384px; height: 246px;
    background: linear-gradient(135deg, var(--panel-gold-light), var(--panel-gold));
    display: flex; flex-direction: column; align-items: center;
    padding-top: 30px;
  }
  .monogram {
    width: 96px; height: 96px;
    border-radius: 50%;
    background: radial-gradient(circle, rgba(167,122,44,.45), rgba(167,122,44,.12));
  }
  .crystal {
    position: absolute;
    width: 6px; height: 6px; border-radius: 50%;
    background: var(--crystal);
    box-shadow: 0 0 2px rgba(0,0,0,.25);
  }
  .couple-names {
    font-family: "Pinyon Script", cursive;
    font-size: 34px;
    line-height: 1;
    margin-top: 10px;
  }
  .wedding-date {
    font-size: 16px;
    letter-spacing: 4px;
    margin-top: 6px;
  }

  /* Open card: pocket holding three graded inserts */
  .open-card {
    position: absolute;
    left: 620px; top: 160px;
    width: 540px; height: 560px;
    box-shadow: 0 2px 8px rgba(60, 40, 25, .18);
  }
  .insert {
    position: absolute;
    left: 50%;
    transform: translateX(-50%);
    box-shadow: 0 1px 4px rgba(60, 40, 25, .2);
  }
  .insert-main {
    top: 22px; width: 500px; height: 520px;
    background: var(--insert-cream);
    text-align: center;
    padding-top: 30px;
  }
  .insert-second {
    top: 340px; width: 470px; height: 200px;
    background: var(--insert-cream-2);
  }
  .insert-third {
    top: 366px; width: 440px; height: 180px;
    background: var(--insert-cream-3);
  }
  .pocket {
    position: absolute;
    left: 0; bottom: 0;
    width: 540px; height: 168px;
    background: linear-gradient(135deg, var(--pocket-gold-light), var(--pocket-gold));
    clip-path: polygon(0 28px, 28px 0, 512px 0, 540px 28px, 540px 100%, 0 100%);
  }

  .quote {
    font-size: 14px;
    line-height: 1.3;
    letter-spacing: .4px;
  }
  .quote-author {
    font-size: 11px;
    margin-top: 2px;
  }
  .names-row {
    display: flex; align-items: center; justify-content: center;
    gap: 12px;
    margin: 18px 0 14px;
  }
  .ornament {
    position: relative;
    width: 70px; height: 28px;
    background: var(--ornament-tint);
  }
  .ornament .crystal { top: 11px; }
  .ornament-left .crystal { left: -10px; }
  .ornament-right .crystal { right: -10px; }
  .insert-names {
    font-family: "Pinyon Script", cursive;
    font-size: 30px;
    color: var(--gold-ink);
    line-height: 1;
  }
  .invite-line {
    font-size: 14.5px;
    letter-spacing: .3px;
    line-height: 1.75;
  }
</style>
</head>
<body>

  <section class="cover stripes" aria-label="Card cover">
    <div class="cover-panel">
      <div class="monogram" role="img" aria-label="Couple's gold script monogram K and R"></div>
      <span class="crystal" style="left:172px; top:48px;"></span>
      <span class="crystal" style="left:222px; top:58px;"></span>
      <span class="crystal" style="left:210px; top:82px;"></span>
      <p class="couple-names">Kavita &amp; Rohan</p>
      <p class="wedding-date">30 April 2014</p>
    </div>
  </section>

  <section class="open-card stripes" aria-label="Opened card with pocket and three inserts">
    <article class="insert insert-main" aria-label="Invitation insert">
      <p class="quote">“Two hearts, one journey: love is the quiet thread<br>that binds every season of a shared life.”</p>
      <p class="quote-author">(Elsa Varga)</p>

      <div class="names-row">
        <div class="ornament ornament-left" role="img" aria-label="Gold scroll ornament"><span class="crystal"></span></div>
        <p class="insert-names">Kavita &amp; Rohan</p>
        <div class="ornament ornament-right" role="img" aria-label="Gold scroll ornament"><span class="crystal"></span></div>
      </div>

      <p class="invite-line">request the pleasure of your company</p>
      <p class="invite-line">at their marriage on Saturday 30 April 2014</p>
      <p class="invite-line">at five o'clock, Halmos Villa, Kertesz str 12., 1125 Budapest</p>
      <p class="invite-line">reception and dinner immediately following the ceremony</p>
    </article>
    <div class="insert insert-second" aria-label="Second insert"></div>
    <div class="insert insert-third" aria-label="Third insert"></div>
    <div class="pocket" aria-label="Gold pocket"></div>
  </section>

</body>
</html>
```